Purely Larkmoor Soap business needs a soap box design

Update 10/3/16 The soap box that I will be using is attached and would like the open circle in the upper right hand corner and vertical
Have attached a suggestion for a style, but open to all designs
My soaps will be more for the mid to high end consumer that wants a natural soap
Would love a box that may be used as a universal soap box

Target Market(s)

high end clients

Industry/Entity Type

Business

Colors
abd036
1b1b1b

Requirements
Must have
• The colors in my logo....green,white and black
• Update 10/3/16 The soap box that I will be using is attached and would like the open circle in the upper right hand corner and the soap box to be horizontal.
Nice to have
• I would like a design that would allow me to add a scent label so I can use a single design box, but not mandatory.
• Keeping with the name "Purely Larkmoor Soap" I would like a simple, but elegant soap box.

```html
<!DOCTYPE html>
<html lang="en">
<head>
<meta charset="utf-8">
<title>Purely Larkmoor Soap — Box Dieline</title>
<link href="https://fonts.googleapis.com/css2?family=Montserrat:wght@600&family=Parisienne&family=Special+Elite&display=swap" rel="stylesheet">
<style>
  :root {
    --sage: #8a9b62;
    --ink: #1b1b1b;
    --brand-ink: #2a2a2a;
    --paper: #ffffff;
    --cut-line: #474747;
  }
  html, body {
    margin: 0;
    padding: 0;
    width: 1200px;
    height: 1000px;
    overflow: hidden;
    background: var(--paper);
  }
  .dieline {
    display: block;
    width: 1200px;
    height: 1000px;
  }
  .panel { stroke: var(--cut-line); stroke-width: 2; }
  .panel--ink { fill: var(--ink); }
  .panel--sage { fill: var(--sage); }
  .panel--paper { fill: var(--paper); stroke: none; }
  .flap-copy {
    font-family: "Montserrat", sans-serif;
    font-weight: 600;
    font-size: 9.5px;
    word-spacing: 3px;
    fill: var(--paper);
  }
  .brand-name {
    font-family: "Parisienne", cursive;
    font-weight: 400;
    font-size: 33px;
  }
  .brand-tagline {
    font-family: "Special Elite", monospace;
    font-size: 12px;
    letter-spacing: 2.4px;
  }
  .on-paper { fill: var(--brand-ink); }
  .on-sage { fill: var(--paper); }
  .brand-dot--sage { fill: var(--sage); }
  .brand-dot--paper { fill: var(--paper); }
</style>
</head>
<body>
<svg class="dieline" viewBox="0 0 1200 1000" xmlns="http://www.w3.org/2000/svg" aria-label="Purely Larkmoor Soap box dieline">
  <!-- top tuck flap -->
  <path class="panel panel--ink" d="M343 259 V171 L437 150 H763 L857 171 V259 Z"/>
  <text class="flap-copy" x="597" y="212" text-anchor="middle">your text your text your text your text your text your text</text>
  <text class="flap-copy" x="597" y="225" text-anchor="middle">your text your text your text your text your text your text</text>

  <!-- side flaps -->
  <path class="panel panel--sage" d="M437 259 H272 Q249 259 249 282 V462 Q249 485 272 485 H437 Z"/>
  <path class="panel panel--sage" d="M763 259 H928 Q951 259 951 282 V462 Q951 485 928 485 H763 Z"/>

  <!-- front face -->
  <rect class="panel--paper" x="437" y="259" width="326" height="226"/>
  <circle class="brand-dot--sage" cx="600" cy="338" r="24"/>
  <text class="brand-name on-paper" x="600" y="414" text-anchor="middle">Purely Larkmoor Soap</text>
  <text class="brand-tagline on-paper" x="600" y="437" text-anchor="middle">handcrafted soap</text>

  <!-- bottom tuck flap -->
  <path class="panel panel--ink" d="M343 485 H857 V573 L763 594 H437 L343 573 Z"/>
  <text class="flap-copy" x="597" y="527" text-anchor="middle">your text your text your text your text your text your text</text>
  <text class="flap-copy" x="597" y="540" text-anchor="middle">your text your text your text your text your text your text</text>

  <!-- back face -->
  <path class="panel panel--sage" d="M437 594 H763 V823 L754 873 H446 L437 823 Z"/>
  <circle class="brand-dot--paper" cx="600" cy="679" r="24"/>
  <text class="brand-name on-sage" x="600" y="755" text-anchor="middle">Purely Larkmoor Soap</text>
  <text class="brand-tagline on-sage" x="600" y="778" text-anchor="middle">handcrafted soap</text>
</svg>
</body>
</html>
```